Velvet Lantern Gala 2014

We're looking to create an 8 1/2" x11" print design using certain elements that we provide.

This is for an invitation/program cover for a Velvet Lantern Gala - so the design has to have a classy look using a set number of colors - GOLD, PURPLE, GREEN - white can also be used as accent or boarder elements.

Please use the file OBVEK 2014 for inspiration and direction. The design MUST connect to that file.

The final design should cause a WOW! factor and play off / or be a companion to design we will upload. (see files)

Requirements
Must have
• Dimension size 8 1/2'' x 11'' (bleed to the end)
St. Augustine Seal to remain (can be small)
A Mardi Gras Mask or person in mask behind front elements which should use transparency
Event location, date, time
Files appropriate for printing - with a semi-transparent object in file
Nice to have
• Key elements like shown on the OBVEK 2014 file
Purple as a key color - either as background or like feathers on picture
10th Annual must show nicely
FONTS: New Century Schoolbook LT and Spinwerad

```html
<!DOCTYPE html>
<html lang="en">
<head>
<meta charset="utf-8">
<title>Velvet Lantern Gala 2014</title>
<link href="https://fonts.googleapis.com/css2?family=Bangers&family=Marcellus+SC&family=Playfair+Display:wght@900&family=Tinos&family=Cinzel:wght@700&display=swap" rel="stylesheet">
<style>
  :root {
    --ink: #050405;
    --gold: #b39a2c;
    --gold-bright: #ffe21a;
    --purple: #4e1f73;
    --purple-deep: #2f0f4a;
    --violet: #8a2be2;
    --parchment: #b49a72;
    --parchment-light: #c9b48e;
    --white: #ffffff;
    --silver: #7d7c80;
  }
  html, body { margin: 0; padding: 0; overflow: hidden; background: var(--ink); }
  .invitation {
    position: relative; width: 900px; height: 1200px; overflow: hidden;
    background: var(--ink);
  }
  .damask-backdrop {
    position: absolute; inset: 0;
    background:
      radial-gradient(ellipse 260px 220px at 790px 140px, rgba(179,154,44,.35), transparent 70%),
      radial-gradient(ellipse 280px 240px at 800px 900px, rgba(179,154,44,.35), transparent 70%),
      radial-gradient(ellipse 260px 320px at 60px 420px, rgba(179,154,44,.28), transparent 70%),
      radial-gradient(ellipse 300px 200px at 520px 90px, rgba(179,154,44,.25), transparent 70%),
      var(--ink);
  }
  .mask-photo {
    position: absolute; left: 0; top: 260px; width: 560px; height: 940px;
    background:
      radial-gradient(ellipse 160px 320px at 170px 280px, rgba(138,43,226,.85), transparent 75%),
      radial-gradient(ellipse 300px 220px at 230px 760px, rgba(125,124,128,.95), rgba(60,58,64,.8) 60%, transparent 85%),
      radial-gradient(ellipse 200px 130px at 200px 920px, rgba(78,31,115,.8), transparent 80%);
  }
  .scroll {
    position: absolute; left: 305px; top: 45px; width: 580px; height: 785px;
    border-radius: 18px;
    background: linear-gradient(160deg, var(--parchment-light), var(--parchment) 55%, #9c8260);
  }
  .seal {
    position: absolute; left: 160px; top: 35px; width: 216px; height: 216px;
    border-radius: 50%; background: var(--gold);
    display: flex; align-items: center; justify-content: center; text-align: center;
  }
  .seal__name {
    font-family: "Cinzel", serif; font-weight: 700; font-size: 24px; line-height: 1.2;
    color: var(--purple);
  }
  .text { position: absolute; left: 330px; width: 470px; text-align: center; margin: 0; }
  .host {
    top: 186px; font-family: "Cinzel", serif; font-weight: 700; font-size: 29px;
    line-height: 38px; color: var(--purple);
  }
  .request { top: 266px; font-family: "Tinos", serif; font-size: 15px; color: var(--white); }
  .edition { position: absolute; left: 425px; top: 290px; width: 340px; height: 160px; }
  .edition__num {
    position: absolute; left: 0; top: 0; font-family: "Playfair Display", serif; font-weight: 900;
    font-size: 150px; line-height: 150px; color: var(--purple); -webkit-text-stroke: 2px var(--white);
  }
  .edition__suffix {
    position: absolute; left: 162px; top: 22px; font-family: "Playfair Display", serif; font-weight: 900;
    font-size: 74px; line-height: 74px; color: var(--purple); -webkit-text-stroke: 1.5px var(--white);
  }
  .edition__label {
    position: absolute; left: 165px; top: 96px; font-family: "Tinos", serif;
    font-size: 42px; line-height: 42px; color: var(--white);
  }
  .gala-title {
    position: absolute; left: 340px; top: 452px; width: 462px; height: 58px;
    border-radius: 10px; background: rgba(255,255,255,.5);
    display: flex; align-items: center; justify-content: center;
    font-family: "Bangers", cursive; font-size: 44px; letter-spacing: 2px;
    color: var(--gold-bright); -webkit-text-stroke: 1.5px #3a2a05;
  }
  .when {
    top: 525px; font-family: "Marcellus SC", serif; font-size: 21px; line-height: 30px;
    color: var(--purple); font-weight: bold;
  }
  .where {
    top: 622px; font-family: "Tinos", serif; font-size: 21px; line-height: 28px; color: var(--white);
  }
  .dress-code {
    position: absolute; left: 418px; top: 920px; width: 454px; height: 216px;
    border-radius: 14px; background: rgba(120,120,125,.55); box-sizing: border-box;
    padding: 26px 22px 0 0; text-align: right;
    font-family: "Bangers", cursive; color: var(--gold-bright); -webkit-text-stroke: 1px #2a2000;
    font-size: 26px; line-height: 33px; letter-spacing: 1px;
  }
  .dress-code p { margin: 0; }
  .dress-code .dress-code__rule { font-size: 36px; line-height: 38px; }
</style>
</head>
<body>
<main class="invitation">
  <div class="damask-backdrop" role="img" aria-label="Black background with gold damask flourishes"></div>
  <div class="mask-photo" role="img" aria-label="Silver masquerade mask with tall purple feathers"></div>
  <div class="scroll" role="img" aria-label="Aged parchment scroll"></div>

  <div class="seal"><span class="seal__name">Oakbrook<br>Academy</span></div>

  <p class="text host">The Guild of<br>Oakbrook Alumni</p>
  <p class="text request">request your presence at our</p>

  <div class="edition">
    <span class="edition__num">10</span>
    <span class="edition__suffix">th</span>
    <span class="edition__label">Annual</span>
  </div>

  <h1 class="gala-title">Velvet Lantern Gala</h1>

  <p class="text when">Saturday<br>February 22, 2014<br>7PM – 12AM</p>
  <p class="text where">Harborview Civic Hall<br>1800 Civic Hall Promenade<br>ATLANTA, GEORGIA</p>

  <section class="dress-code">
    <p>A Semi Formal Affair</p>
    <p>Tuxedo, Dark Suits and Ties</p>
    <p class="dress-code__rule">NO HATS ALLOWED</p>
    <p>Tea Length or Formal Dresses</p>
    <p>Cost : $75.00</p>
  </section>
</main>
</body>
</html>
```